High End Pet Treat Soft Packaging Label

I am looking for a front label design for dog treats to be sold in a soft package (possibly standing) like a zip lock bag. The product name is "RUFUS'S MORSELS" and is basically dehydrated chicken breast. I would like to incorporate the attached file that I have been playing with. I have also attached a copy of the original photo. Product keys are safety, quality, purity, freshness and taste. This will be a high end product so I need a label that will project the high quality of the product and stand out from all the others on the shelf. I am also thinking about a craft paper type of look but I am open.

Target Market(s)

Target market is US adult dog owners in metro areas with higher disposable incomes who see their dogs as family members and are willing to spend more for the best products for their pets.

Industry/Entity Type

Pet

Colors

Designer to choose colors to be used in the design.

Requirements
Must have
• Depiction of a golden retriever...Rufus.

```html
<!DOCTYPE html>
<html lang="en">
<head>
<meta charset="utf-8">
<title>Rufus's Morsels – Front Label</title>
<link rel="stylesheet" href="https://fonts.googleapis.com/css2?family=Cormorant+SC:wght@500;600&display=swap">
<style>
  :root {
    --page: #ffffff;
    --border: #6f8f9c;
    --stripe-light: #e3dfcf;
    --stripe-dark: #d8d1be;
    --ink: #2f5f6e;
    --frame-tan: #b1a68e;
    --frame-teal: #4f7485;
    --frame-cream: #e6e1d2;
    --photo-dark: #6f6583;
    --photo-mid: #9a8ea6;
    --photo-warm: #b79f7e;
  }
  * { margin: 0; padding: 0; box-sizing: border-box; }
  html, body {
    width: 1200px; height: 1200px; overflow: hidden;
    background: var(--page);
  }
  .canvas { position: relative; width: 1200px; height: 1200px; }

  .label {
    position: absolute;
    left: 262px; top: 150px; width: 679px; height: 896px;
    border: 8px solid var(--border);
    background: repeating-linear-gradient(90deg,
      var(--stripe-light) 0 19px, var(--stripe-dark) 19px 38px);
    font-family: "Cormorant SC", "Times New Roman", serif;
    color: var(--ink);
  }

  .product-name {
    position: absolute;
    left: 85px; top: 70px;
    font-size: 66px; font-weight: 600; letter-spacing: 1px;
    line-height: 1; white-space: nowrap;
  }

  .portrait-frame {
    position: absolute;
    left: 63px; top: 151px; width: 534px; height: 531px;
    background: var(--frame-tan);
    padding: 9px 9px 10px 9px;
  }
  .portrait-frame .teal {
    width: 100%; height: 100%;
    background: var(--frame-teal);
    padding: 20px;
  }
  .portrait-frame .cream {
    width: 100%; height: 100%;
    background: var(--frame-cream);
    padding: 5px;
  }
  .portrait {
    width: 100%; height: 100%;
    background:
      radial-gradient(ellipse 45% 55% at 50% 58%, var(--photo-warm), transparent 70%),
      linear-gradient(180deg, var(--photo-dark), var(--photo-mid) 45%, var(--photo-dark));
  }

  .tagline {
    position: absolute;
    left: 0; right: 0; top: 700px;
    text-align: center;
    font-size: 44px; font-weight: 500; letter-spacing: 0.5px;
    line-height: 1; white-space: nowrap;
  }
  .tagline-rule {
    position: absolute;
    left: 67px; width: 526px; top: 753px;
    height: 3px; background: var(--frame-teal);
  }
  .description {
    position: absolute;
    left: 0; right: 0; top: 770px;
    text-align: center;
    font-size: 32px; font-weight: 500; letter-spacing: 0.5px;
    line-height: 45px; white-space: nowrap;
  }
</style>
</head>
<body>
<main class="canvas">
  <section class="label">
    <h1 class="product-name">Rufus’s Morsels</h1>

    <div class="portrait-frame">
      <div class="teal">
        <div class="cream">
          <div class="portrait" role="img" aria-label="Portrait photo of Rufus, a smiling golden retriever, posterized in soft purple and gold tones"></div>
        </div>
      </div>
    </div>

    <p class="tagline">Only the Best for my Buddies</p>
    <div class="tagline-rule"></div>
    <p class="description">fresh and tasty dog treats<br>made with only the finest ingredients</p>
  </section>
</main>
</body>
</html>
```